Wordpress Identity for Innovation Firm

Lumen Harbor Partners is an innovation and investment firm based in Los Angeles.

We are seeking a designer that can help create our company identity and Wordpress site.

The attached Design Brief provides more details.

Designers Responsibility:

1) Company Identity

The designer will create the company identity.
Attached is a file that contains a type font that I like a lot.
No logo design is required.

The Lumen Harbor Partners type font should become the company identity.
The attached document provides an overview of company type font identities that we like.

2) Wordpress Theme & Design

The designer will select existing Wordpress Themes that meet our design desires, and present them as part of the design proposal.

We will make our selection based on the selected Wordpress Theme(s), which the designer will creatively adapt with the new company identity.

Target Market(s)

We anticipate the website being mostly accessed by the US, Canada and European countries.

Our target audience includes the following:

• Corporations, companies, startups, non-profits
• Banks, venture capital, private equity, investors
• Incubators, accelerators, innovation clusters, research labs, universities
• Ad agencies, marketing agencies, digital agencies, media, press

Industry/Entity Type

Investment

Number of Pages Required

1 page

Font styles to use
Sans Serif
Other font styles liked:
• See attached design brief materials. The Font will represent the brand identity!

Requirements
Must have
• The ability to scroll through information top to bottom is important to us.
• This is in line with today's Wordpress themes.
• The website must be able to function across devices (desktop, tablet, phone).
• The top 5 web browsers and platforms (Mac/PC/Android/iOS)
• Contact us link or information field
Nice to have
• It would be nice to have a moving image in the background, such as:
• https://tidalshowcase.examplesite.com
• The Wordpress theme of the moving image or video should be relevant to our overall Technology Innovation theme.
• Key words:
• Technology Innovation
• Digital
• Business
• Transportation
• Advanced Vehicles (auto, boat, airplane, rail, space)
• Space
• Venture Capital
• Investing
Should not have
• eCommerce

```html
<!DOCTYPE html>
<html lang="en">
<head>
<meta charset="utf-8">
<title>Lumen Harbor Partners</title>
<link rel="stylesheet" href="https://fonts.googleapis.com/css2?family=Open+Sans:wght@400;600;700&display=swap">
<style>
:root{
  --blue:#1f8fd6;
  --blue-dark:#1776b4;
  --navy:#2c3446;
  --ink:#121316;
  --text:#4a4f57;
  --muted:#8a9099;
  --line:#d9dde2;
  --field:#e9ecef;
  --footer:#e4e6e9;
  --white:#ffffff;
}
*{box-sizing:border-box;margin:0;padding:0}
html,body{width:1200px;height:2796px;overflow:hidden}
body{font-family:"Open Sans",Arial,sans-serif;color:var(--text);background:var(--white)}
.site-header{height:48px;display:flex;align-items:center;justify-content:space-between;padding:0 60px 0 36px;background:var(--white)}
.brand{display:flex;flex-direction:column}
.brand-name{font-size:15px;font-weight:700;color:var(--blue);letter-spacing:1px;text-transform:uppercase}
.brand-tag{font-size:7px;color:var(--muted);letter-spacing:.6px;text-transform:uppercase}
.main-nav{display:flex;gap:26px}
.main-nav a{font-size:11px;font-weight:600;color:var(--ink);text-decoration:none;text-transform:uppercase}
.main-nav a.active{color:var(--blue)}
.hero{position:relative;height:544px;background:linear-gradient(120deg,#b9c6cf 0%,#6f8796 35%,#d2d7d6 60%,#8ea3ae 100%)}
.hero-card{position:absolute;left:380px;top:132px;width:440px;padding:22px 30px 22px;background:rgba(255,255,255,.86);text-align:center}
.hero-card h1{font-size:22px;font-weight:700;color:var(--blue);text-transform:uppercase;letter-spacing:.5px;margin-bottom:10px}
.hero-card p{font-size:10px;line-height:1.55;color:var(--text);margin-bottom:14px}
.btn{display:inline-block;font-weight:600;text-transform:uppercase;text-decoration:none}
.btn-solid{background:var(--blue);color:var(--white);font-size:10px;padding:6px 14px}
.hero-dots{position:absolute;left:0;right:0;top:534px;display:flex;justify-content:center;gap:10px}
.hero-dots span{width:12px;height:12px;border-radius:50%;background:var(--ink)}
.hero-dots span.on{background:var(--blue)}
.feature{position:relative;display:flex;align-items:center}
.feature-navy{height:388px;background:var(--navy)}
.feature-dark{height:292px;background:var(--ink)}
.feature-art{position:absolute;border-radius:4px}
.feature-navy .feature-art{left:100px;top:24px;width:440px;height:340px;background:radial-gradient(circle at 50% 50%,#4a5467 0%,#343c50 70%,var(--navy) 100%)}
.feature-dark .feature-art{left:800px;top:56px;width:300px;height:180px;background:linear-gradient(135deg,#1d4f7a 0%,#2a8ad0 55%,#1b2230 100%)}
.feature-copy{position:absolute;width:400px}
.feature-navy .feature-copy{left:620px;top:52px}
.feature-dark .feature-copy{left:180px;top:40px;width:420px}
.feature-copy h2{font-size:25px;line-height:1.18;font-weight:700;color:var(--blue);text-transform:uppercase;margin-bottom:12px}
.feature-copy p{font-size:10px;line-height:1.65;color:#c9ced6;margin-bottom:18px}
.btn-outline{border:2px solid var(--blue);color:var(--blue);font-size:17px;font-weight:400;padding:6px 22px}
.feature-navy .btn-outline{margin-left:170px}
.services{height:648px;padding:16px 0 0 180px}
.services h2{font-size:33px;font-weight:400;color:var(--ink);text-transform:uppercase;padding-bottom:8px;border-bottom:1px solid var(--line);width:840px;margin-bottom:12px}
.services .intro{font-size:14px;line-height:1.5;color:var(--text);width:820px;margin-bottom:40px}
.service-grid{display:grid;grid-template-columns:repeat(3,240px);column-gap:40px;row-gap:30px}
.service-icon{width:34px;height:34px;border-radius:50%;background:#3b4250;display:flex;align-items:center;justify-content:center;margin-bottom:8px}
.service h3{font-size:12px;font-weight:600;color:var(--blue);text-transform:uppercase;margin-bottom:5px}
.service p{font-size:9.5px;line-height:1.55;color:var(--muted)}
.services .cta{display:flex;justify-content:center;width:840px;margin-top:48px}
.btn-cta{border:2px solid var(--blue);color:var(--blue);font-size:23px;font-weight:400;padding:8px 26px}
.brands{position:relative;height:420px;background:linear-gradient(160deg,#3d3d3d 0%,#1c1c1c 45%,#4a4a4a 75%,#222 100%)}
.brands-name{position:absolute;left:90px;top:352px;font-size:22px;font-weight:600;color:#cfcfcf;letter-spacing:1px}
.contact{height:380px;padding:26px 0 0 240px;display:flex;gap:0}
.contact h2{font-size:33px;font-weight:600;color:var(--ink);text-transform:uppercase;border-bottom:1px solid var(--line);padding-bottom:8px;margin-bottom:14px;width:840px}
.contact-body{display:flex}
.contact-form{width:420px}
.contact-form label{display:block;font-size:9px;font-weight:600;color:var(--blue);text-transform:uppercase;margin-bottom:3px}
.field{height:26px;background:var(--field);font-size:9px;color:var(--muted);padding:7px 8px;margin-bottom:10px}
.field.tall{height:116px}
.btn-submit{background:var(--blue);color:var(--white);font-size:9px;padding:5px 12px}
.contact-address{margin-left:40px}
.contact-address h3{font-size:10px;font-weight:600;color:var(--ink);text-transform:uppercase;margin-bottom:8px}
.contact-address p{font-size:9.5px;line-height:1.6;color:var(--muted)}
.site-footer{height:76px;background:var(--footer);display:flex;align-items:center;justify-content:space-between;padding:0 100px 0 240px}
.site-footer p{font-size:9px;color:var(--muted)}
.social{display:flex;gap:8px}
.social span{width:20px;height:20px;border-radius:50%;background:#3b4250}
</style>
</head>
<body>
<header class="site-header">
  <div class="brand">
    <span class="brand-name">Lumen Harbor Partners</span>
    <span class="brand-tag">Innovation &amp; investment firm · Los Angeles</span>
  </div>
  <nav class="main-nav">
    <a class="active" href="#">Home</a>
    <a href="#">About</a>
    <a href="#">Services</a>
    <a href="#">Media</a>
    <a href="#">Contact</a>
  </nav>
</header>

<section class="hero" role="img" aria-label="Background photo of a team planning ideas on a glass board with sticky notes">
  <div class="hero-card">
    <h1>Lumen Harbor Partners</h1>
    <p>Lumen Harbor Partners is an innovation and investment firm based in Los Angeles. We back founders building technology, mobility and digital products, pairing patient capital with hands-on guidance from a seasoned team of operators.</p>
    <a class="btn btn-solid" href="#">Learn more!</a>
  </div>
  <div class="hero-dots"><span class="on"></span><span></span><span></span><span></span></div>
</section>

<section class="feature feature-navy">
  <div class="feature-art" role="img" aria-label="Illustration of a desktop computer connected to technology and business icons"></div>
  <div class="feature-copy">
    <h2>Lorem ipsum is<br>simply dummy text<br>of the printing</h2>
    <p>Lorem ipsum dolor sit amet, consectetur adipiscing elit, sed do eiusmod tempor incididunt ut labore et dolore magna aliqua. Ut enim ad minim veniam, quis nostrud exercitation ullamco laboris nisi ut aliquip ex ea commodo consequat.</p>
    <a class="btn btn-outline" href="#">Read more</a>
  </div>
</section>

<section class="feature feature-dark">
  <div class="feature-copy">
    <h2>Lorem ipsum is<br>simply dummy text<br>of the printing</h2>
    <p>Lorem ipsum dolor sit amet, consectetur adipiscing elit, sed do eiusmod tempor incididunt ut labore et dolore magna aliqua. Ut enim ad minim veniam, quis nostrud exercitation ullamco laboris nisi ut aliquip ex ea commodo consequat.</p>
    <a class="btn btn-outline" href="#">Read more</a>
  </div>
  <div class="feature-art" role="img" aria-label="Illustration of a monitor and phone playing video"></div>
</section>

<section class="services">
  <h2>Services</h2>
  <p class="intro">Lorem Ipsum is simply dummy text of the printing and typesetting industry. Lorem Ipsum has been the industry's standard dummy text ever since the 1500s.</p>
  <div class="service-grid">
    <div class="service">
      <div class="service-icon"><svg width="16" height="16" viewBox="0 0 16 16"><circle cx="8" cy="8" r="5" fill="none" stroke="#fff" stroke-width="2"/><circle cx="8" cy="8" r="1.5" fill="#fff"/></svg></div>
      <h3>Technology innovation</h3>
      <p>Lorem ipsum dolor sit amet, consectetur adipiscing elit, sed do eiusmod tempor incididunt ut labore et dolore magna.</p>
    </div>
    <div class="service">
      <div class="service-icon"><svg width="16" height="16" viewBox="0 0 16 16"><rect x="2" y="2" width="5" height="5" fill="#fff"/><rect x="9" y="2" width="5" height="5" fill="#fff"/><rect x="2" y="9" width="5" height="5" fill="#fff"/><rect x="9" y="9" width="5" height="5" fill="#fff"/></svg></div>
      <h3>Digital</h3>
      <p>Lorem ipsum dolor sit amet, consectetur adipiscing elit, sed do eiusmod tempor incididunt ut labore et dolore magna.</p>
    </div>
    <div class="service">
      <div class="service-icon"><svg width="16" height="16" viewBox="0 0 16 16"><circle cx="8" cy="5" r="3" fill="#fff"/><path d="M2 15c0-4 3-5 6-5s6 1 6 5z" fill="#fff"/></svg></div>
      <h3>Business</h3>
      <p>Lorem ipsum dolor sit amet, consectetur adipiscing elit, sed do eiusmod tempor incididunt ut labore et dolore magna.</p>
    </div>
    <div class="service">
      <div class="service-icon"><svg width="16" height="16" viewBox="0 0 16 16"><path d="M2 9l12-6-5 12-1-5z" fill="#fff"/></svg></div>
      <h3>Transportation</h3>
      <p>Lorem ipsum dolor sit amet, consectetur adipiscing elit, sed do eiusmod tempor incididunt ut labore et dolore magna.</p>
    </div>
    <div class="service">
      <div class="service-icon"><svg width="16" height="16" viewBox="0 0 16 16"><rect x="2" y="6" width="12" height="5" rx="1" fill="#fff"/><circle cx="5" cy="12" r="2" fill="#fff"/><circle cx="11" cy="12" r="2" fill="#fff"/></svg></div>
      <h3>Advanced vehicles</h3>
      <p>Lorem ipsum dolor sit amet, consectetur adipiscing elit, sed do eiusmod tempor incididunt ut labore et dolore magna.</p>
    </div>
    <div class="service">
      <div class="service-icon"><svg width="16" height="16" viewBox="0 0 16 16"><path d="M2 9a6 6 0 0 1 12 0z" fill="#fff"/><rect x="7.2" y="9" width="1.6" height="5" fill="#fff"/></svg></div>
      <h3>Investing</h3>
      <p>Lorem ipsum dolor sit amet, consectetur adipiscing elit, sed do eiusmod tempor incididunt ut labore et dolore magna.</p>
    </div>
  </div>
  <div class="cta"><a class="btn btn-cta" href="#">Get started now</a></div>
</section>

<section class="brands" role="img" aria-label="Dark collage of company lettering as a background band">
  <span class="brands-name">Lumen Harbor Partners</span>
</section>

<section class="contact">
  <div>
    <h2>Contact</h2>
    <div class="contact-body">
      <form class="contact-form">
        <label>Your name</label>
        <div class="field">Enter your name</div>
        <label>Email</label>
        <div class="field">Enter your email</div>
        <label>Message</label>
        <div class="field tall">Write your message here</div>
        <span class="btn btn-submit">Submit</span>
      </form>
      <div class="contact-address">
        <h3>Address</h3>
        <p>1250 Harbor Crest Ave, Suite 400<br>Los Angeles, CA 90017<br>Tel: (310) 555-0148<br>hello@lumenharbor.example</p>
      </div>
    </div>
  </div>
</section>

<footer class="site-footer">
  <p>© 2024 Lumen Harbor Partners. All rights reserved.</p>
  <div class="social"><span></span><span></span></div>
</footer>
</body>
</html>
```